National Sales Conference

We need a cool one page flyer inviting our sales partners to a National Sales Training Class.

Most important event in 5 years! Do not even consider missing it

Details of Sales Meeting
Nov 10th - 11th in Dallas, TX
Nov 10th (welcome party) 7-9pm

Preliminary Agenda
Nov, 10th 7-9pm Welcome Reception

Nov 11th and 12th 9-4 Tillpoint Drill Week Sales training. Learn the tools you need to become more relevant in the marketplace as we launch multiple new cutting edge products and services. Many vendors will be on hand to personally meet you and provide the tools and marketing information you need.

Location of event
Kelbrook Plaza Lodge West
2876 Harlowmere Pkwy.
Fort Worth, TX 76392
FREE Shuttle from DFW!
Updates

Please put the Brightwater Vendor Solutions logo at the TOP left and the Quillstone Remit logo make it small and near the bottom

Add the following TEXT. 

*** This event is so important our CEO, Marcus Delong has decided that we are covering all of the expenses! That's right, we will provide the sleeping room based on double occupancy, all meals, and with 10 deals in 90 days we will even reimburse your airfare if a flight is necessary. 

Be sure to include the RSVP information and lines for the to print out and check if they are coming or not as indicated in the original brief. 

This flyer will be sent to our sales agents VIA Email in PDF. Therefore, if we need to make it 2 pages so it is not so cluttered, I'm okay with that. 

Target Market(s)

Our Sales Agents

Industry/Entity Type

Training

Requirements
Must have
• One page! High energy will a strong call to action.
• Needs a small fill in the blank for an RSVP
• Name _______________
• Check Box YES! I will gladly attend. _____ # attending
• Check Box Can't make it.
• Fax RSVP to 775-319-2740 or email marcusd@brightwaterco.example

```html
<!DOCTYPE html>
<html lang="en">
<head>
<meta charset="utf-8">
<title>National Sales Conference</title>
<link rel="stylesheet" href="https://fonts.googleapis.com/css2?family=Oswald:wght@600;700&family=Cinzel:wght@500&family=Didact+Gothic&display=swap">
<style>
  :root {
    --blue: #1d6fc6;
    --box-blue: #3b73c9;
    --navy: #0f2a55;
    --green: #8dc63f;
    --lime: #9acd3c;
    --ink: #1b1b1b;
    --text-blue: #3a6fc4;
    --white: #ffffff;
    --logo-blue: #2a3a92;
    --logo-green: #6cae2d;
    --deco: #eef0f3;
    --deco-arrow: #f2d2cc;
  }
  * { margin: 0; padding: 0; box-sizing: border-box; }
  html, body { width: 1200px; height: 2454px; overflow: hidden; background: var(--white); }
  .flyer { position: relative; width: 1200px; height: 2454px; background: var(--white); font-family: "Didact Gothic", "Century Gothic", sans-serif; color: var(--ink); }

  .hero-photo {
    position: absolute; left: 0; top: 0; width: 1200px; height: 1134px;
    background:
      radial-gradient(ellipse at 78% 40%, #e9d9cc 0%, rgba(233,217,204,0) 30%),
      radial-gradient(ellipse at 48% 48%, #d9cbbf 0%, rgba(217,203,191,0) 22%),
      radial-gradient(ellipse at 22% 52%, #cfd3d8 0%, rgba(207,211,216,0) 24%),
      linear-gradient(180deg, #f6f8fa 0%, #e8edf2 45%, #aeb6bf 78%, #5d6470 100%);
  }

  .logo { display: flex; align-items: center; font-family: "Oswald", sans-serif; font-weight: 700; }
  .logo-brightwater { position: absolute; left: 52px; top: 64px; gap: 18px; color: var(--logo-blue); font-size: 50px; line-height: 1.02; }
  .logo-brightwater .mark { width: 72px; height: 72px; background: var(--logo-blue); flex: none; }

  .headline { position: absolute; left: 48px; top: 748px; font-family: "Oswald", sans-serif; font-weight: 700; text-transform: uppercase; line-height: 0.86; }
  .headline .line { display: block; -webkit-text-stroke: 4px var(--white); paint-order: stroke fill; }
  .headline .most { color: var(--blue); font-size: 190px; letter-spacing: -2px; }
  .headline .important { color: var(--blue); font-size: 126px; letter-spacing: -1px; margin-top: 6px; }
  .headline .event { color: var(--ink); font-size: 98px; letter-spacing: -1px; margin-top: 4px; }

  .tagline { position: absolute; left: 0; top: 1178px; width: 1200px; text-align: center; font-family: "Cinzel", serif; font-weight: 500; color: var(--text-blue); font-size: 46px; letter-spacing: 1px; }

  .details-band { position: absolute; left: 0; top: 1276px; width: 1200px; height: 196px; background: var(--green); }
  .rsvp-short { position: absolute; left: 50px; top: 64px; font-size: 23px; line-height: 36px; color: var(--ink); }
  .meeting { position: absolute; right: 100px; top: 22px; text-align: right; font-size: 30px; line-height: 40px; color: var(--ink); }
  .meeting .title { text-transform: uppercase; }

  .agenda-title { position: absolute; left: 0; top: 1510px; width: 1200px; text-align: center; font-family: "Cinzel", serif; font-weight: 500; color: var(--text-blue); font-size: 48px; }

  .agenda-deco { position: absolute; left: 860px; top: 1590px; width: 320px; height: 420px; }

  .agenda-box { position: absolute; top: 1608px; height: 162px; padding: 18px 22px; font-size: 32px; line-height: 38px; color: var(--navy); }
  .agenda-box .title { text-transform: uppercase; }
  .agenda-box.reception { left: 157px; width: 425px; background: var(--box-blue); }
  .agenda-box.training { left: 596px; width: 452px; background: var(--lime); padding-top: 14px; line-height: 36px; }
  sup { font-size: 0.6em; line-height: 0; }

  .intro { position: absolute; left: 157px; top: 1796px; width: 900px; font-size: 30px; line-height: 38px; color: var(--text-blue); }

  .expenses { position: absolute; left: 157px; top: 1966px; width: 891px; font-size: 23px; line-height: 31px; color: var(--ink); }
  .expenses strong { color: var(--blue); font-weight: 400; }

  .venue-photo { position: absolute; left: 162px; top: 2110px; width: 420px; height: 206px;
    background: linear-gradient(180deg, #4b78b8 0%, #8fb0d6 38%, #b57d5a 58%, #8a6a52 74%, #6b6f73 100%); }

  .location { position: absolute; left: 594px; top: 2110px; width: 376px; height: 206px; background: var(--box-blue); color: var(--white); padding: 22px 0 0 34px; font-size: 22px; }
  .location .title { text-transform: uppercase; margin-bottom: 14px; }
  .location .address { line-height: 32px; opacity: 0.85; }
  .location .shuttle { margin-top: 8px; }

  .rsvp-form { position: absolute; left: 157px; top: 2336px; width: 891px; display: flex; justify-content: space-between; font-size: 22px; line-height: 35px; color: var(--ink); }
  .rsvp-form .fill { display: inline-block; border-bottom: 2px solid var(--ink); height: 24px; vertical-align: baseline; }
  .rsvp-form .fill.name { width: 300px; }
  .rsvp-form .fill.count { width: 60px; }
  .rsvp-form .box { display: inline-block; width: 20px; height: 20px; border: 2px solid var(--ink); margin-right: 10px; vertical-align: -2px; }
  .rsvp-contact { text-align: right; }
  .logo-quillstone { justify-content: flex-end; gap: 10px; color: var(--logo-green); font-size: 26px; line-height: 35px; }
  .logo-quillstone .mark { width: 24px; height: 24px; border-radius: 50%; background: var(--logo-green); }
</style>
</head>
<body>
<main class="flyer">
  <div class="hero-photo" role="img" aria-label="Photo of three smiling business professionals seated at a meeting"></div>

  <div class="logo logo-brightwater"><span class="mark"></span><span>Brightwater<br>Vendor Solutions</span></div>

  <h1 class="headline">
    <span class="line most">Most</span>
    <span class="line important">Important</span>
    <span class="line event">Event in 5 Years</span>
  </h1>

  <p class="tagline">DO NOT EVEN CONSIDER MISSING IT</p>

  <section class="details-band">
    <p class="rsvp-short">Fax RSVP to 775-319-2740<br>Email : marcusd@brightwaterco.example</p>
    <div class="meeting">
      <p class="title">Details of Sales Meeting</p>
      <p>Nov 10<sup>th</sup> - 11<sup>th</sup> in Dallas, TX</p>
      <p>Nov 10<sup>th</sup> (welcome party) 7-9pm</p>
    </div>
  </section>

  <h2 class="agenda-title">PRELIMINARY AGENDA</h2>

  <svg class="agenda-deco" viewBox="0 0 320 420" aria-hidden="true">
    <rect x="150" y="150" width="46" height="270" fill="var(--deco)"/>
    <rect x="220" y="90" width="46" height="330" fill="var(--deco)"/>
    <path d="M0 400 L250 70" stroke="var(--deco-arrow)" stroke-width="10" fill="none"/>
    <path d="M220 60 L270 40 L262 96 Z" fill="var(--deco-arrow)"/>
  </svg>

  <div class="agenda-box reception">
    <p>Nov, 10<sup>th</sup> 7-9pm</p>
    <p class="title">Welcome Reception</p>
  </div>
  <div class="agenda-box training">
    <p>Nov 11<sup>th</sup> and 12<sup>th</sup> 9-4</p>
    <p class="title">Tillpoint Drill Week</p>
    <p class="title">Sales Training</p>
  </div>

  <p class="intro">Learn the tools you need to become more relevant in the marketplace as we launch multiple new cutting edge products and services. Many vendors will be on hand to personally meet you and provide the tools and marketing information you need.</p>

  <p class="expenses"><strong>***</strong> This event is so important our CEO, Marcus Delong has decided that we are covering all of the expenses! That's right, we will provide the sleeping room based on double occupancy, all meals, and with 10 deals in 90 days we will even reimburse your airfare if a flight is necessary.</p>

  <div class="venue-photo" role="img" aria-label="Photo of the hotel venue exterior at dusk"></div>
  <section class="location">
    <p class="title">Location of Event</p>
    <p class="address">Kelbrook Plaza Lodge West<br>2876 Harlowmere Pkwy.<br>Fort Worth, TX 76392</p>
    <p class="shuttle">FREE Shuttle from DFW!</p>
  </section>

  <section class="rsvp-form">
    <div class="rsvp-fields">
      <p>Name <span class="fill name"></span></p>
      <p><span class="box"></span>YES! I will gladly attend. <span class="fill count"></span> # attending</p>
      <p><span class="box"></span>Can't make it.</p>
    </div>
    <div class="rsvp-contact">
      <p>Fax RSVP to 775-319-2740</p>
      <p>or email marcusd@brightwaterco.example</p>
      <div class="logo logo-quillstone"><span class="mark"></span><span>Quillstone Remit</span></div>
    </div>
  </section>
</main>
</body>
</html>
```